Restaurant Menu Design for Meal Prep offered in a food display cooler at a local Gym

I am looking for a menu design with the following items . I would like a workable copy if possible so in the future we can change pricing on this file , or change items . This file will be uploaded on a USB drive and then plugged into a TV. Please ensure a JPEG file is included so this will also work on this TV.

Have a look at our website , www.vantorelkitchen.com for ideas for design that represent the brand appropriately.
The below are the menu items that we would need displayed along with their pricing.

BREAKFAST MEAL PREP ITEMS
Blueberry Pancakes $12.00
Full Throttle Burrito $10.95

LUNCH/DINNER MEAL PREP OPTIONS
BBQ Glazed Salmon $16.50
Cheeseburger Bowl $13.50
Chicken Alfredo $12.00
Pesto Chicken Pasta $12.00
Chicken Parmesan $13.00
Taco Bowl $14.00
Steak Bite and Green Stir Fry $12.00
Asian Chicken Teriyaki $12.00
Galloway Stir Fry $15.95

I will attach our logo below, this will need to be on the design. The "heading" (for example breakfast meal prep items and lunch/dinner meal prep options) for the menu should also be on the design.

Ive attached a couple of photos that you need to add to your design.

Target Market(s)

This will be displayed in a GYM

Industry/Entity Type

Meal Prep + Fitness Industry

Requirements
Must have
• Vantorel Logo and Photos attached
Nice to have
• Maybe incorporate something that represents working out or healthy lifestyle in design without going too overboard

```html
<!DOCTYPE html>
<html lang="en">
<head>
<meta charset="utf-8">
<title>Vantorel Healthy Kitchen – Meal Prep Menu</title>
<link rel="stylesheet" href="https://fonts.googleapis.com/css2?family=Open+Sans:wght@400;600;700&family=Montserrat:wght@800&display=swap">
<style>
  :root {
    --bg: #f1f2f3;
    --green: #8cc63e;
    --text-grey: #8a8a8a;
    --logo-grey: #878787;
    --sketch-line: #c9cccf;
    --sketch-fill: #e6e8ea;
    --wood: #dde4e8;
    --wood-dark: #c7d0d6;
    --plate: #f7f7f5;
    --pancake: #d6a767;
    --pasta: #8f9d4f;
  }
  * { margin: 0; padding: 0; box-sizing: border-box; }
  html, body { width: 1200px; height: 675px; overflow: hidden; background: var(--bg); }
  .menu-board {
    position: relative; width: 1200px; height: 675px; overflow: hidden;
    background: var(--bg);
    font-family: "Open Sans", Arial, sans-serif;
  }
  .sketch { position: absolute; }
  .sketch--left { left: 66px; top: 40px; width: 172px; height: 140px; }
  .sketch--right { left: 975px; top: 30px; width: 170px; height: 160px; }

  .welcome {
    position: absolute; top: 74px; left: 0; width: 1200px; text-align: center;
    font-size: 20px; font-weight: 400; color: var(--text-grey); letter-spacing: 0.3px;
  }
  .brand-name {
    position: absolute; top: 108px; left: 0; width: 1200px; text-align: center;
    font-family: "Montserrat", Arial, sans-serif; font-weight: 800;
    font-size: 60px; line-height: 66px; color: var(--logo-grey); letter-spacing: 2px;
  }
  .brand-tagline {
    position: absolute; top: 170px; left: 0; width: 1200px; text-align: center;
    font-size: 19px; font-weight: 700; color: var(--green); letter-spacing: -0.4px;
  }
  .brand-tagline .divider { display: inline-block; margin: 0 10px; }

  .section-title {
    position: absolute; text-align: center; color: var(--green);
    font-size: 24px; font-weight: 600; line-height: 29px;
  }
  .section-title--breakfast { left: 57px; width: 252px; top: 301px; }
  .section-title--lunch { left: 566px; width: 282px; top: 256px; }

  .menu-list { position: absolute; list-style: none; }
  .menu-list--breakfast { left: 57px; top: 365px; width: 233px; }
  .menu-list--lunch { left: 586px; top: 320px; width: 232px; }
  .menu-list--stirfry { left: 862px; top: 406px; width: 235px; }
  .menu-item {
    display: flex; align-items: baseline; height: 28.6px;
    font-size: 15px; color: var(--text-grey); white-space: nowrap;
  }
  .menu-item .leader {
    flex: 1; margin: 0 1px; min-width: 4px; height: 1px;
    border-bottom: 2px dotted #9a9a9a; transform: translateY(-2px);
  }

  .photo { position: absolute; }
  .photo--pancakes { left: 289px; top: 264px; width: 236px; height: 182px; }
  .photo--pasta { left: 854px; top: 229px; width: 236px; height: 167px; }
  .photo-band { position: absolute; left: 0; top: 548px; width: 1200px; height: 127px; }
</style>
</head>
<body>
<main class="menu-board">
  <svg class="sketch sketch--left" viewBox="0 0 172 140" role="img" aria-label="Line sketch of a plate with fruit and vegetables">
    <circle cx="80" cy="70" r="60" fill="var(--sketch-fill)" stroke="var(--sketch-line)" stroke-width="1.5"/>
    <circle cx="80" cy="70" r="52" fill="none" stroke="var(--sketch-line)" stroke-width="1"/>
  </svg>
  <svg class="sketch sketch--right" viewBox="0 0 170 160" role="img" aria-label="Line sketch of a bowl with sliced apple and kiwi">
    <circle cx="62" cy="88" r="55" fill="var(--sketch-fill)" stroke="var(--sketch-line)" stroke-width="1.5"/>
    <circle cx="62" cy="88" r="47" fill="none" stroke="var(--sketch-line)" stroke-width="1"/>
  </svg>

  <header>
    <p class="welcome">WELCOME TO</p>
    <h1 class="brand-name">VANTOREL</h1>
    <p class="brand-tagline">HEALTHY KITCHEN<span class="divider">|</span>MEAL PREP</p>
  </header>

  <section aria-labelledby="breakfast-title">
    <h2 id="breakfast-title" class="section-title section-title--breakfast">BREAKFAST MEAL<br>PREP ITEMS</h2>
    <ul class="menu-list menu-list--breakfast">
      <li class="menu-item"><span>Blueberry Pancakes</span><span class="leader"></span><span>$12.00</span></li>
      <li class="menu-item"><span>Full Throttle Burrito</span><span class="leader"></span><span>$10.95</span></li>
    </ul>
    <svg class="photo photo--pancakes" viewBox="0 0 236 182" role="img" aria-label="Photo of a stack of blueberry pancakes on a white plate on a wooden table">
      <defs>
        <radialGradient id="pancake-tone" cx="0.52" cy="0.5" r="0.55">
          <stop offset="0" stop-color="var(--pancake)"/>
          <stop offset="0.28" stop-color="#e9dcc8"/>
          <stop offset="0.45" stop-color="var(--plate)"/>
          <stop offset="0.62" stop-color="var(--wood)"/>
          <stop offset="1" stop-color="var(--wood-dark)"/>
        </radialGradient>
      </defs>
      <path d="M22 20 C 70 6, 160 4, 212 16 C 226 40, 232 100, 222 150 C 180 176, 70 178, 24 162 C 8 120, 4 60, 22 20 Z" fill="url(#pancake-tone)"/>
    </svg>
  </section>

  <section aria-labelledby="lunch-title">
    <h2 id="lunch-title" class="section-title section-title--lunch">LUNCH/DINNER MEAL<br>PREP OPTIONS</h2>
    <ul class="menu-list menu-list--lunch">
      <li class="menu-item"><span>BBQ Glazed Salmon</span><span class="leader"></span><span>$16.50</span></li>
      <li class="menu-item"><span>Cheeseburger Bowl</span><span class="leader"></span><span>$13.50</span></li>
      <li class="menu-item"><span>Chicken Alfredo</span><span class="leader"></span><span>$12.00</span></li>
      <li class="menu-item"><span>Pesto Chicken Pasta</span><span class="leader"></span><span>$12.00</span></li>
      <li class="menu-item"><span>Chicken Parmesan</span><span class="leader"></span><span>$13.00</span></li>
      <li class="menu-item"><span>Taco Bowl</span><span class="leader"></span><span>$14.00</span></li>
    </ul>
    <ul class="menu-list menu-list--stirfry">
      <li class="menu-item"><span>Steak Bite &amp; Green Stir Fry</span><span class="leader"></span><span>$12.00</span></li>
      <li class="menu-item"><span>Asian Chicken Teriyaki</span><span class="leader"></span><span>$12.00</span></li>
      <li class="menu-item"><span>Galloway Stir Fry</span><span class="leader"></span><span>$15.95</span></li>
    </ul>
    <svg class="photo photo--pasta" viewBox="0 0 236 167" role="img" aria-label="Photo of pesto chicken pasta with broccoli in a white bowl on a wooden table">
      <defs>
        <radialGradient id="pasta-tone" cx="0.55" cy="0.5" r="0.55">
          <stop offset="0" stop-color="var(--pasta)"/>
          <stop offset="0.3" stop-color="#b9bf8e"/>
          <stop offset="0.46" stop-color="var(--plate)"/>
          <stop offset="0.62" stop-color="var(--wood)"/>
          <stop offset="1" stop-color="var(--wood-dark)"/>
        </radialGradient>
      </defs>
      <path d="M20 14 C 80 2, 170 2, 222 14 C 234 50, 234 110, 222 150 C 170 166, 70 166, 22 152 C 6 110, 6 50, 20 14 Z" fill="url(#pasta-tone)"/>
    </svg>
  </section>

  <svg class="photo-band" viewBox="0 0 1200 127" preserveAspectRatio="none" role="img" aria-label="Photos of a mushroom and tomato flatbread pizza and a cheese and pepper pizza">
    <defs>
      <linearGradient id="pizza-flatbread" x1="0" y1="0" x2="1" y2="0">
        <stop offset="0" stop-color="#4b4139"/>
        <stop offset="0.35" stop-color="#8a5a3a"/>
        <stop offset="0.6" stop-color="#b0603a"/>
        <stop offset="1" stop-color="#6e4a34"/>
      </linearGradient>
      <linearGradient id="pizza-cheese" x1="0" y1="0" x2="1" y2="0">
        <stop offset="0" stop-color="#e2c9a8"/>
        <stop offset="0.25" stop-color="#e0a25a"/>
        <stop offset="0.7" stop-color="#d48a48"/>
        <stop offset="1" stop-color="#b6c0c6"/>
      </linearGradient>
    </defs>
    <path d="M0 50 C 60 40, 110 26, 170 16 C 300 6, 450 8, 600 6 L 600 127 L 0 127 Z" fill="url(#pizza-flatbread)"/>
    <path d="M604 6 C 760 4, 900 6, 1040 12 C 1110 16, 1160 22, 1200 30 L 1200 127 L 604 127 Z" fill="url(#pizza-cheese)"/>
    <path d="M0 58 C 120 40, 260 22, 420 14 L 420 17 C 260 26, 120 44, 0 62 Z" fill="#ffffff" opacity="0.8"/>
    <path d="M760 16 C 900 14, 1060 20, 1200 36 L 1200 40 C 1060 25, 900 19, 760 19 Z" fill="#ffffff" opacity="0.8"/>
  </svg>
</main>
</body>
</html>
```